Corvale Real Estate

I manage 2 firms. The first one is Pelmora and the logo is in blue (see the file) but i need a design for my business card for the second firm called CORVALE IMMOBILIER. This one is in charge of Real estate developer.

Colors
3176b5

```html
<!DOCTYPE html>
<html lang="en">
<head>
<meta charset="utf-8">
<title>Corvale Immobilier – Business Card</title>
<link href="https://fonts.googleapis.com/css2?family=Lato:wght@400;700;900&display=swap" rel="stylesheet">
<style>
  :root {
    --brand-blue: #3176b5;
    --brand-blue-deep: #2c62ac;
    --brand-grey: #a3a3a5;
    --ink: #1f1f22;
    --card-white: #fbf8f8;
    --divider: #e2dede;
    --backdrop: #e9e9eb;
  }
  * { box-sizing: border-box; margin: 0; padding: 0; }
  html, body {
    width: 1200px; height: 782px; overflow: hidden;
    background: var(--backdrop);
    font-family: "Lato", Arial, sans-serif;
  }
  .sheet {
    width: 1200px; height: 782px;
    display: flex; align-items: center; justify-content: center; gap: 40px;
  }
  .card {
    position: relative;
    width: 540px; height: 310px;
    overflow: hidden;
    box-shadow: 0 6px 18px rgba(0,0,0,0.18);
  }

  /* Front */
  .card-front { background: var(--card-white); }
  .brand-block {
    position: absolute; left: 30px; top: 118px; width: 220px;
  }
  .brand-name {
    font-weight: 900; font-size: 42px; letter-spacing: 1px;
    color: var(--brand-blue); line-height: 1;
  }
  .brand-sub {
    font-weight: 900; font-size: 42px; letter-spacing: 1px;
    color: var(--brand-blue); line-height: 1; font-size: 17px;
    letter-spacing: 6.3px; margin-top: 4px;
  }
  .divider {
    position: absolute; left: 262px; top: 70px;
    width: 1px; height: 150px; background: var(--divider);
  }
  .contact {
    position: absolute; left: 286px; top: 72px; color: var(--ink);
  }
  .contact-name {
    font-weight: 700; font-size: 21px; color: var(--brand-blue);
    letter-spacing: 0.3px; line-height: 1.05;
  }
  .contact-role { font-size: 14px; margin-bottom: 5px; }
  .contact-line {
    display: flex; align-items: center; gap: 6px;
    font-size: 15px; line-height: 20px;
  }
  .contact-line svg { width: 11px; height: 11px; flex: none; }
  .address { font-size: 15px; line-height: 20px; margin-top: 2px; }
  .base-bands { position: absolute; left: 0; bottom: 0; }

  /* Back */
  .card-back { background: var(--brand-blue-deep); }
  .pattern-field {
    position: absolute; inset: 0;
    background: linear-gradient(135deg, #2f67b3 0%, #2c61ab 100%);
  }
  .back-mark {
    position: absolute; left: 0; right: 0; top: 196px;
    text-align: center;
    font-weight: 900; font-size: 22px; letter-spacing: 2px; color: #ffffff;
  }
</style>
</head>
<body>
<main class="sheet">

  <section class="card card-front" aria-label="Business card front">
    <div class="brand-block">
      <div class="brand-name">CORVALE</div>
      <div class="brand-name brand-sub">IMMOBILIER</div>
    </div>

    <div class="divider"></div>

    <div class="contact">
      <p class="contact-name">JULIEN MARCHAND</p>
      <p class="contact-role">Managing Director</p>
      <p class="contact-line">
        <svg viewBox="0 0 12 12" aria-hidden="true"><path fill="#3176b5" d="M2.5 1h2l1 3-1.4 1a6 6 0 0 0 3 3l1-1.4 3 1v2c0 .6-.5 1-1 1A10 10 0 0 1 1.5 2c0-.5.4-1 1-1z"/></svg>
        044-987 654 321
      </p>
      <p class="contact-line">
        <svg viewBox="0 0 12 12" aria-hidden="true"><rect x="0.5" y="2" width="11" height="8" fill="#3176b5"/><path d="M1 2.5l5 4 5-4" fill="none" stroke="#fff" stroke-width="1"/></svg>
        info@corvale-immo.com
      </p>
      <p class="contact-line">
        <svg viewBox="0 0 12 12" aria-hidden="true"><circle cx="6" cy="6" r="5.5" fill="#3176b5"/><path d="M.8 6h10.4M6 .6c-2.6 3-2.6 7.8 0 10.8M6 .6c2.6 3 2.6 7.8 0 10.8" fill="none" stroke="#fff" stroke-width="0.8"/></svg>
        www.corvale-immo.com
      </p>
      <p class="address">18, Rue des Tanneurs<br>Lyon, France 69002</p>
    </div>

    <svg class="base-bands" width="540" height="40" viewBox="0 0 540 40" aria-hidden="true">
      <rect x="0" y="26" width="310" height="14" fill="var(--brand-blue)"/>
      <polygon points="296,40 308,14 540,14 540,40" fill="var(--brand-grey)"/>
    </svg>
  </section>

  <section class="card card-back" aria-label="Business card back">
    <div class="pattern-field" role="img" aria-label="Faint repeating brand pattern over the blue background"></div>
    <div class="back-mark">CORVALE</div>
  </section>

</main>
</body>
</html>
```